Modern Corporate Brochure For Australian Real Estate Agency

We need a corporate 10 page A4 brochure for a Australian Real Estate agency with information for our clients and referral partners.

Main colour scheme: #238b53

Examples of designs:
https://quillmarsh.net/item/8-page-corporate-business-brochure/5827314

https://quillmarsh.net/item/brochure/27461983

https://quillmarsh.net/item/the-company-profile/38150726

https://quillmarsh.net/item/brochure-pack-a4trifold-leafletbusiness-card/736182

Target Market(s)

Professional Australians

Industry/Entity Type

Real Estate

Font styles to use
Sans Serif

Requirements
Must have
• Use of multiple greens from the logo

```html
<!DOCTYPE html>
<html lang="en">
<head>
<meta charset="utf-8">
<title>Ridgeline Property Group – Brochure Spreads</title>
<link href="https://fonts.googleapis.com/css2?family=Lato:ital,wght@0,400;0,700;0,900;1,400;1,700&display=swap" rel="stylesheet">
<style>
:root{
  --bg:#80848d;
  --green:#3da64f;
  --green-brand:#238b53;
  --green-mid:#4db86a;
  --green-dark:#2b7d4c;
  --green-deep:#1f5f3a;
  --mint:#9de3a6;
  --charcoal:#474747;
  --charcoal-2:#444444;
  --ink:#333333;
  --white:#ffffff;
}
*{margin:0;padding:0;box-sizing:border-box}
html,body{width:784px;height:1200px;overflow:hidden}
body{background:var(--bg);font-family:'Lato',sans-serif;color:var(--ink);position:relative}
.spread{position:absolute;left:56px;width:672px;height:475px;background:var(--white);overflow:hidden;box-shadow:0 4px 14px rgba(0,0,0,.3)}
.spread--outer{top:84px}
.spread--inner{top:579px}
.spread svg.shapes{position:absolute;left:0;top:0;width:672px;height:475px}
.t{position:absolute;font-size:7.3px;line-height:9.4px}
.green{color:var(--green)}
.intro{left:19px;top:13px;width:300px}
.quote-mark{left:17px;top:46px;font-size:44px;line-height:44px;font-weight:900;color:var(--green)}
.testimonial{font-style:italic;width:145px}
.testimonial--one{left:19px;top:88px}
.testimonial--two{left:173px;top:88px}
.attribution{font-size:6.5px;line-height:8px;color:var(--green);font-weight:700}
.attribution--one{left:19px;top:154px}
.attribution--two{left:173px;top:143px}
.contact{left:166px;color:var(--white);width:170px}
.contact--brisbane{top:339px}
.contact--gladstone{top:405px}
.contact .city{color:var(--green);padding-left:11px}
.contact .row{display:flex;align-items:flex-start;gap:5px}
.contact .row svg{flex:0 0 6px;width:6px;height:6px;margin-top:1.8px}
.contact .row.indent{padding-left:11px}
.social{position:absolute;top:436px;width:23px;height:23px;border-radius:50%;background:var(--white);border:2px solid var(--green)}
.cover-title{left:369px;top:66px;color:var(--white);font-size:15px;line-height:18px;letter-spacing:.2px}
.cover-title .accent{color:var(--green);font-weight:900}
.cover-title .big{font-size:20px;line-height:22px;font-weight:900;display:block}
.cover-rule{position:absolute;left:384px;top:127px;width:71px;height:2px;background:var(--white)}
.brand{position:absolute;display:flex;align-items:center;gap:5px;font-weight:700;color:var(--green-dark);white-space:nowrap}
.brand .mark{width:9px;height:9px;background:var(--green-brand)}
.brand--cover{left:514px;top:63px;font-size:10px}
.brand--about{left:15px;top:44px;font-size:8.5px}
.about-title{left:15px;top:64px;font-size:13px;line-height:15px;font-weight:700;color:var(--green)}
.body{font-size:6.4px;line-height:8.1px}
.about-body{left:15px;top:96px;width:316px}
.illustration{position:absolute;left:111px;top:175px;width:49px;height:50px;border-radius:6px;background:linear-gradient(135deg,#e3f3e8,#bfe3ca)}
.pm-title{left:168px;top:177px;font-size:10px;line-height:12px;font-weight:700;color:var(--green)}
.pm-body{left:168px;top:205px;width:160px}
.pm-list{left:168px;top:294px;width:165px;list-style:none}
.pm-list li{position:relative;padding-left:10px}
.pm-list li::before{content:"";position:absolute;left:2px;top:3px;width:2.4px;height:2.4px;border-radius:50%;background:var(--ink)}
.pm-note{left:168px;top:408px;width:162px;font-style:italic;color:var(--green)}
.mission-title{left:16px;top:322px;font-size:15px;line-height:18px;color:var(--white)}
.mission-quote{left:16px;top:355px;width:131px;font-size:9px;line-height:12.2px;font-style:italic;color:var(--white)}
.region-title{font-size:13px;line-height:15px;font-weight:700}
.gladstone-title{right:15px;top:16px;text-align:right;color:var(--green-deep)}
.gladstone-title .accent{color:var(--green)}
.service-right{right:57px;text-align:right;width:265px}
.service-right h3,.service-left h3{font-size:6.6px;line-height:8px;font-weight:700}
.service-right h3{color:var(--green-deep)}
.service--gm{top:39px}
.service--gs{top:93px}
.brisbane-title{left:349px;top:228px}
.brisbane-title .accent{color:var(--green);display:block}
.brisbane-title .sub{color:var(--white);font-size:11.5px}
.service-left{left:401px;width:260px;color:var(--white)}
.service-left h3{color:var(--green)}
.service--bm{top:281px}
.service--bs{top:331px}
.service--bp{top:379px}
.service--bd{top:427px}
</style>
</head>
<body>

<!-- Outer spread: back cover and front cover -->
<section class="spread spread--outer">
  <svg class="shapes" viewBox="0 0 672 475" aria-hidden="false">
    <defs>
      <linearGradient id="fadedBuilding" x1="0" y1="0" x2="1" y2="1">
        <stop offset="0" stop-color="#f4f4f4"/>
        <stop offset="1" stop-color="#d9d9d9"/>
      </linearGradient>
      <linearGradient id="skyline" x1="0" y1="0" x2="0" y2="1">
        <stop offset="0" stop-color="#a9c3d8"/>
        <stop offset=".45" stop-color="#e8c9a0"/>
        <stop offset=".62" stop-color="#8a8478"/>
        <stop offset="1" stop-color="#6f8591"/>
      </linearGradient>
    </defs>
    <rect role="img" aria-label="Faded photo of a glass office tower" x="0" y="0" width="336" height="475" fill="url(#fadedBuilding)"/>
    <polygon points="0,306 336,120 336,218 0,397" fill="var(--green)"/>
    <polygon points="0,300 60,268 78,335 0,380" fill="var(--green-dark)"/>
    <polygon points="200,210 336,120 336,175" fill="#2c8552"/>
    <polygon points="0,397 336,218 336,475 0,475" fill="var(--charcoal)"/>
    <polygon role="img" aria-label="Photo of a city skyline beside a river at sunset" points="336,210 672,345 672,475 336,475" fill="url(#skyline)"/>
    <polygon points="336,67 353,75 353,190 336,185" fill="var(--green)"/>
    <polygon points="336,165 353,172 353,210 336,205" fill="var(--mint)"/>
    <polygon points="486,112 672,200 672,228 486,140" fill="var(--green-dark)"/>
    <polygon points="486,132 672,222 672,345 486,252" fill="var(--green)"/>
    <polygon points="640,235 672,200 672,250" fill="var(--mint)"/>
    <polygon points="353,0 486,0 486,257 353,188" fill="var(--charcoal)"/>
  </svg>

  <p class="t intro"><span class="green">Ridgeline Property Group</span> is committed to developing strong relationships with both our landlords and tenants to ensure each property is always professionally managed and never vacant. Our job as intermediaries is built on trust and communication, and our results exemplify this.</p>
  <div class="t quote-mark">&ldquo;</div>
  <p class="t testimonial testimonial--one">Thank you Tom Keller from Ridgeline Property for your professional approach in selling my house at 9 Ironbark Cres Gladstone. I gained maximum price for my investment with minimum fuss. I highly recommend Tom for any realty matters.</p>
  <p class="t attribution attribution--one">REID ASHCOMBE<br>GLADSTONE LANDLORD</p>
  <p class="t testimonial testimonial--two">Many thanks and I hope to deal with you again in the future- you have provided absolutely brilliant service as well as outstanding communication. Thanks again and all the best.</p>
  <p class="t attribution attribution--two">MARISOL – TENANT</p>

  <div class="t contact contact--brisbane">
    <div class="city">BRISBANE</div>
    <div class="row"><svg viewBox="0 0 6 6"><rect x=".4" y="1" width="5.2" height="4" fill="none" stroke="#3da64f" stroke-width=".7"/><path d="M.4 1 3 3.2 5.6 1" fill="none" stroke="#3da64f" stroke-width=".7"/></svg>info@ridgelineproperty.com.au</div>
    <div class="row"><svg viewBox="0 0 6 6"><path d="M1 .5 2.2.5 2.7 2 2 2.6Q2.8 4 3.6 4.2L4.1 3.5 5.5 4V5.3Q1.5 5.4.6 1Z" fill="#3da64f"/></svg>(07) 3100 4821</div>
    <div class="row"><svg viewBox="0 0 6 6"><rect x="1.5" y=".5" width="3" height="1.5" fill="#3da64f"/><rect x=".5" y="2.2" width="5" height="2.3" fill="#3da64f"/><rect x="1.5" y="4" width="3" height="1.6" fill="#3da64f"/></svg>(07) 4900 3165 (fax)</div>
    <div class="row"><svg viewBox="0 0 6 6"><path d="M3 .3A2 2 0 0 1 5 2.3C5 3.6 3 5.8 3 5.8S1 3.6 1 2.3A2 2 0 0 1 3 .3Z" fill="#3da64f"/><circle cx="3" cy="2.3" r=".7" fill="#474747"/></svg>58 Ferrier Lane, Fortitude Valley</div>
    <div class="row indent">Brisbane 4006</div>
  </div>
  <div class="t contact contact--gladstone">
    <div class="city">GLADSTONE</div>
    <div class="row"><svg viewBox="0 0 6 6"><rect x=".4" y="1" width="5.2" height="4" fill="none" stroke="#3da64f" stroke-width=".7"/><path d="M.4 1 3 3.2 5.6 1" fill="none" stroke="#3da64f" stroke-width=".7"/></svg>gladstone@ridgelineproperty.com.au</div>
    <div class="row"><svg viewBox="0 0 6 6"><path d="M1 .5 2.2.5 2.7 2 2 2.6Q2.8 4 3.6 4.2L4.1 3.5 5.5 4V5.3Q1.5 5.4.6 1Z" fill="#3da64f"/></svg>(07) 4900 2847</div>
    <div class="row"><svg viewBox="0 0 6 6"><rect x="1.5" y=".5" width="3" height="1.5" fill="#3da64f"/><rect x=".5" y="2.2" width="5" height="2.3" fill="#3da64f"/><rect x="1.5" y="4" width="3" height="1.6" fill="#3da64f"/></svg>(07) 4900 3165 (fax)</div>
    <div class="row"><svg viewBox="0 0 6 6"><path d="M3 .3A2 2 0 0 1 5 2.3C5 3.6 3 5.8 3 5.8S1 3.6 1 2.3A2 2 0 0 1 3 .3Z" fill="#3da64f"/><circle cx="3" cy="2.3" r=".7" fill="#474747"/></svg>2/41 Marlow St, Gladstone Central</div>
    <div class="row indent">Gladstone 4680</div>
  </div>

  <span class="social" style="left:20px"></span>
  <span class="social" style="left:51px"></span>
  <span class="social" style="left:82px"></span>

  <h1 class="t cover-title">A <span class="accent">NEW LEVEL</span><br>OF SERVICE IN<span class="big">PROPERTY</span></h1>
  <div class="cover-rule"></div>
  <div class="brand brand--cover"><span class="mark"></span>RIDGELINE PROPERTY GROUP</div>
</section>

<!-- Inner spread: about us and services -->
<section class="spread spread--inner">
  <svg class="shapes" viewBox="0 0 672 475">
    <defs>
      <linearGradient id="fadedTower" x1="0" y1="0" x2="1" y2="1">
        <stop offset="0" stop-color="#ececec"/>
        <stop offset="1" stop-color="#d6d6d6"/>
      </linearGradient>
    </defs>
    <line x1="0" y1="83" x2="146" y2="83" stroke="var(--green)" stroke-width="1.5"/>
    <polygon points="0,190 158,285 0,285" fill="var(--green-dark)"/>
    <polygon points="0,220 68,224 0,285" fill="#1f6a40"/>
    <polygon points="68,224 158,285 52,285" fill="#2f8a52"/>
    <rect x="0" y="285" width="158" height="190" fill="var(--green-mid)"/>
    <rect role="img" aria-label="Faded photo of a glass office tower" x="336" y="0" width="336" height="475" fill="url(#fadedTower)"/>
    <polygon points="336,74 672,235 672,345 336,165" fill="#3fae5c"/>
    <polygon points="336,165 672,345 672,475 336,475" fill="var(--charcoal-2)"/>

    <g fill="var(--green-mid)">
      <polygon points="619.5,62 631.25,41.5 654.75,41.5 666.5,62 654.75,82.5 631.25,82.5"/>
      <polygon points="619.5,128 631.25,107.5 654.75,107.5 666.5,128 654.75,148.5 631.25,148.5"/>
      <polygon points="347.5,296 359.25,275.5 382.75,275.5 394.5,296 382.75,316.5 359.25,316.5"/>
      <polygon points="347.5,344 359.25,323.5 382.75,323.5 394.5,344 382.75,364.5 359.25,364.5"/>
      <polygon points="347.5,392 359.25,371.5 382.75,371.5 394.5,392 382.75,412.5 359.25,412.5"/>
      <polygon points="347.5,440 359.25,419.5 382.75,419.5 394.5,440 382.75,460.5 359.25,460.5"/>
    </g>
    <g fill="none" stroke="#fff" stroke-width="1.6" stroke-linejoin="round">
      <path d="M634 63 643 55 652 63M636 61V70H641V65H645V70H650V61"/>
      <rect x="635" y="120" width="16" height="16" rx="2"/>
      <path d="M639 133V128M643 133V124M647 133V130"/>
      <path d="M363 300 372 292 381 300M365 298V307H370V302H374V307H379V298"/>
      <rect x="363" y="336" width="16" height="16" rx="2"/>
      <path d="M367 349V344M371 349V340M375 349V346"/>
      <path d="M364 389H368L377 383V401L368 395H364Z"/>
      <path d="M380 388 383 386M380 392H384M380 396 383 398"/>
      <rect x="363" y="432" width="16" height="11"/>
      <path d="M366 440 370 436 373 438 377 434M371 443V449M367 449H375"/>
    </g>
  </svg>

  <div class="brand brand--about"><span class="mark"></span>RIDGELINE PROPERTY GROUP</div>
  <h2 class="t about-title">Get to know us better</h2>
  <p class="t body about-body"><b>Ridgeline Property Group</b> is one of Queensland's fastest growing property agencies. Our team are driven, focused, trained, and have proven results delivering better service and achieving superior results for their clients than any other agency in the market place. Our team collectively manage over 600 properties and have over 50 years' experience between them. In total we manage an asset portfolio worth in excess of 200 million and have only been operating since August 2012. Experiencing that kind of growth predominantly via referral means that we must be doing something right. Our clients and associates strongly believe in what we do and appreciate the dedication they receive when allowing Ridgeline Property Group the opportunity to manage or sell their largest asset</p>

  <div class="illustration" role="img" aria-label="Line illustration of a hand holding a money bag and buildings"></div>
  <h3 class="t pm-title">Property Management<br>Specialists</h3>
  <p class="t body pm-body">It is common to find that within the overwhelming majority of real estate offices the property management department is the most under resourced. It's no wonder investors move from one agency to another in search of a decent property manager and agency to work with. If you are experiencing any, or all of the practices listed below then you need to seriously consider moving the management of your property to Ridgeline Property Group immediately.</p>
  <ul class="t body pm-list">
    <li>Extended periods of vacancy</li>
    <li>Lower rental yields than you expect</li>
    <li>Not receiving routing inspections on time, or at all</li>
    <li>A lack of communication from your property manager</li>
    <li>Poor service skills when dealing with staff within your managing agency</li>
    <li>Dealing with a property manager who isn't intimate with the rental market</li>
    <li>A constant turnover of property managers within the agency managing your property</li>
    <li>Not having easy access to information such as financial statements, routine reports &amp; leases</li>
  </ul>
  <p class="t body pm-note">Our property managers receive regular training with independent industry professionals and organisations to ensure they are aware of all legislative changes as they are made that allows them to deal with whatever comes their way comfortably &amp; efficiently.</p>

  <h2 class="t mission-title">Our Mission</h2>
  <p class="t mission-quote">"To provide a superior service that is unmatched in the real estate industry and ensure that all Ridgeline Property Group clients achieve the highest possible yields and sale prices for their properties."</p>

  <h2 class="t region-title gladstone-title"><span class="accent">GLADSTONE's</span> Fastest Growing Property Group</h2>
  <div class="t body service-right service--gm">
    <h3>GLADSTONE Property Management</h3>
    <p>Our average vacancy rate at any given time is under 5% and our properties generate 6% higher rents than our competitors. Why is that? Because we strategically aim to have our leases expiring at the right times of the year when demand is at its highest for any particular area. Not all areas are the same, in fact some areas can deliver rental variations of over 10% if not timed/managed correctly.</p>
  </div>
  <div class="t body service-right service--gs" style="right:55px">
    <h3>GLADSTONE Property Sales</h3>
    <p>Our sales consultants are real people who deliver real results for their clientele. There's no hidden agenda, overpriced listing<br>agreements or advertising packages. We pride ourselves<br>on delivering the best results achievable in the<br>market at any given time and provide<br>a motivated, driven agent<br>determined to impress.</p>
  </div>

  <h2 class="t region-title brisbane-title"><span class="accent">BRISBANE's</span><span class="sub">Leading Property Group</span></h2>
  <div class="t body service-left service--bm">
    <h3>BRISBANE Property Management</h3>
    <p>Our average vacancy rate at any given time is<br>under 5% and our properties generate 6% higher<br>rents than our competitors.</p>
  </div>
  <div class="t body service-left service--bs">
    <h3>BRISBANE Property Sales</h3>
    <p>Only elite agents with the right approach to dealing with people in real estate are offered the opportunity to sell through Ridgeline Property Group</p>
  </div>
  <div class="t body service-left service--bp">
    <h3>BRISBANE Project Marketing</h3>
    <p>We work closely with a number of large and reputable marketing agencies and companies that have the capacity to deliver a large number of sales.</p>
  </div>
  <div class="t body service-left service--bd">
    <h3>BRISBANE Development Management</h3>
    <p>Development management is a niche skill and takes both the academic knowhow and experience to deliver the project through to completion.</p>
  </div>
</section>

</body>
</html>
```